Stationary and Business Card design for Dental office
Stationary design for Harborview Lane Dental of Seattle
Stationary and Business Card design for Dental office - Medical
Creative Brief
Modern
Harborview Lane Dental Of Seattle
4186 Birchmont Rd NW Suite 212 Seattle, WA. 98107
harborviewlanedentalofseattle@mailbox-example.com
www.harborviewlanedentalofseattle-example.com
Please on the back of the card add the logo and also nicely put 1 Date of Appointment______ 2 Time Of Appointment 3 Appointment with ______ 4 Cancellations require 24 hour advance notice
Please use same colors as logo thank you all

```html
<!DOCTYPE html>
<html lang="en">
<head>
<meta charset="utf-8">
<title>Harborview Lane Dental of Seattle – Business Card</title>
<link rel="stylesheet" href="https://fonts.googleapis.com/css2?family=Didact+Gothic&display=swap">
<style>
  :root {
    --backdrop: #e9e7e4;
    --card-white: #ffffff;
    --brand-purple: #5b1a8c;
    --brand-gold: #e3a21a;
    --text-white: #ffffff;
    --shadow: rgba(0, 0, 0, 0.18);
  }
  * { margin: 0; padding: 0; box-sizing: border-box; }
  html, body {
    width: 1200px;
    height: 900px;
    overflow: hidden;
    background: var(--backdrop);
    font-family: "Didact Gothic", "Century Gothic", sans-serif;
  }
  .canvas {
    position: relative;
    width: 1200px;
    height: 900px;
    display: flex;
    align-items: center;
    justify-content: center;
  }
  .business-card {
    position: relative;
    width: 1000px;
    height: 571px;
    background: var(--card-white);
    box-shadow: 0 12px 30px var(--shadow);
    overflow: hidden;
  }
  .card-waves {
    position: absolute;
    inset: 0;
    width: 100%;
    height: 100%;
  }
  .brand-lockup {
    position: absolute;
    left: 430px;
    top: 92px;
    display: flex;
    align-items: center;
    gap: 16px;
  }
  .brand-dot {
    width: 44px;
    height: 44px;
    border-radius: 50%;
    background: var(--brand-purple);
    flex: none;
  }
  .brand-name {
    color: var(--brand-purple);
    font-size: 30px;
    letter-spacing: 1.5px;
    font-variant: small-caps;
    line-height: 1.15;
  }
  .contact-list {
    position: absolute;
    left: 34px;
    top: 398px;
    list-style: none;
    color: var(--text-white);
    font-size: 14.5px;
    letter-spacing: 1px;
    font-variant: small-caps;
    line-height: 1.25;
  }
  .contact-item {
    display: flex;
    align-items: flex-start;
    gap: 8px;
    margin-bottom: 4px;
  }
  .contact-icon {
    width: 15px;
    height: 15px;
    flex: none;
    margin-top: 1px;
  }
  .practice-label {
    position: absolute;
    right: 40px;
    top: 352px;
    color: var(--text-white);
    font-size: 17px;
    letter-spacing: 1.5px;
    font-variant: small-caps;
    text-align: right;
    line-height: 1.3;
  }
</style>
</head>
<body>
<main class="canvas">
  <section class="business-card">
    <svg class="card-waves" viewBox="0 0 1000 571" preserveAspectRatio="none" aria-hidden="true">
      <path fill="#d9d9d9" d="M0 318 C 250 284, 450 346, 660 286 S 900 214, 1000 228 L1000 234 C 900 222, 860 238, 660 294 S 250 292, 0 326 Z"/>
      <path fill="var(--brand-gold)" d="M0 326 C 250 292, 450 354, 660 294 S 900 222, 1000 234 L1000 262 C 900 252, 860 262, 660 312 S 250 312, 0 342 Z"/>
      <path fill="var(--brand-purple)" d="M0 340 C 250 312, 450 370, 660 312 S 900 254, 1000 262 L1000 571 L0 571 Z"/>
    </svg>

    <div class="brand-lockup">
      <span class="brand-dot"></span>
      <div class="brand-name">Harborview Lane Dental<br>of Seattle</div>
    </div>

    <ul class="contact-list">
      <li class="contact-item">
        <svg class="contact-icon" viewBox="0 0 16 16"><circle cx="8" cy="8" r="8" fill="#fff"/><path d="M8 3.2a3 3 0 0 0-3 3c0 2.3 3 6.2 3 6.2s3-3.9 3-6.2a3 3 0 0 0-3-3zm0 4.2a1.2 1.2 0 1 1 0-2.4 1.2 1.2 0 0 1 0 2.4z" fill="var(--brand-purple)"/></svg>
        <span>4186 Birchmont Rd NW Suite 212<br>Seattle, WA. 98107</span>
      </li>
      <li class="contact-item">
        <svg class="contact-icon" viewBox="0 0 16 16"><circle cx="8" cy="8" r="8" fill="#fff"/><path d="M5.2 3.6l1.6 1.8-.8 1.2c.6 1.3 1.5 2.2 2.8 2.8l1.2-.8 1.8 1.6-.9 1.5c-3.3-.3-6.3-3.3-6.6-6.6z" fill="var(--brand-purple)"/></svg>
        <span>206-555-0143</span>
      </li>
      <li class="contact-item">
        <svg class="contact-icon" viewBox="0 0 16 16"><circle cx="8" cy="8" r="8" fill="#fff"/><rect x="5" y="4.5" width="6" height="7" rx="1" fill="var(--brand-purple)"/><rect x="6" y="5.5" width="4" height="3" fill="#fff"/></svg>
        <span>harborviewlanedentalofseattle@mailbox-example.com</span>
      </li>
      <li class="contact-item">
        <svg class="contact-icon" viewBox="0 0 16 16"><circle cx="8" cy="8" r="8" fill="#fff"/><path d="M5.2 3.6l1.6 1.8-.8 1.2c.6 1.3 1.5 2.2 2.8 2.8l1.2-.8 1.8 1.6-.9 1.5c-3.3-.3-6.3-3.3-6.6-6.6z" fill="var(--brand-purple)"/></svg>
        <span>206 555 0178</span>
      </li>
      <li class="contact-item">
        <svg class="contact-icon" viewBox="0 0 16 16"><circle cx="8" cy="8" r="8" fill="#fff"/><circle cx="8" cy="8" r="4" fill="none" stroke="var(--brand-purple)" stroke-width="1.2"/><path d="M4 8h8M8 4c-1.6 2.4-1.6 5.6 0 8M8 4c1.6 2.4 1.6 5.6 0 8" fill="none" stroke="var(--brand-purple)" stroke-width="0.9"/></svg>
        <span>www.harborviewlanedentalofseattle-example.com</span>
      </li>
    </ul>

    <p class="practice-label">Harborview Lane Dental<br>Of Seattle</p>
  </section>
</main>
</body>
</html>
```